Lantern Co. Supplement General Packaging Design

I am looking for a design template to design all of my various supplements and other products around. Meaning that this design should be able to just be able to change around words, up to a few small images, and text to suit my other various products.

The brand name is Lantern Co. and the slogan is: Legends Take Root
This is For an Apple Cider Vinegar Gummy, and include these top three things: Vegan, Gluten Free, Non-GMO somewhere in the design.

I want the design to have a luxurious feel. With some kind of design element where the logo is sort of the secondary aspect of the design.

Target Market(s)

Men age 24-45

Industry/Entity Type

Supplement

Requirements
Must have
• MUST HAVE A "vintage" LOOK AND FEEL. MUST HAVE ANOTHER design element besides the logo. (Something Vintage) MUST USE THE PROVIDED TEMPLATE A PDF IN THE FILES BELOW LABELED " TEMPLATE" and the LOGO PROVIDED under "Lantern Co. 2" OR "Lantern Co.3" whichever is better suited for the design. Bold design. Another color besides black to stand out. Use the lantern co logo which is below in the provided images. The design should go around the logo and fit the same aesthetic. The rest are for inspiration, what I like.

```html
<!DOCTYPE html>
<html lang="en">
<head>
<meta charset="utf-8">
<title>Lantern Co. Apple Cider Vinegar Gummy Label</title>
<link rel="stylesheet" href="https://fonts.googleapis.com/css2?family=Lobster&family=Graduate&family=Oswald:wght@500;600&family=Montserrat:wght@500;700&display=swap">
<style>
  :root {
    --red: #e8413e;
    --red-deep: #a42b2c;
    --ink: #3b3641;
    --ink-deep: #221e27;
    --white: #ffffff;
  }
  html, body {
    margin: 0;
    padding: 0;
    overflow: hidden;
    background: var(--ink);
  }
  .label {
    position: relative;
    width: 1200px;
    height: 957px;
    overflow: hidden;
    background: var(--ink);
  }
  .label__top {
    position: absolute;
    left: 0; top: 0;
    width: 1200px; height: 564px;
    background: var(--red);
  }
  .label__texture {
    position: absolute;
    left: 0; top: 0;
    width: 1200px; height: 564px;
    background:
      radial-gradient(ellipse at 20% 30%, rgba(59, 54, 65, 0.10), transparent 45%),
      radial-gradient(ellipse at 85% 20%, rgba(59, 54, 65, 0.12), transparent 40%),
      radial-gradient(ellipse at 70% 85%, rgba(59, 54, 65, 0.08), transparent 45%);
  }
  .label__art {
    position: absolute;
    left: 0; top: 0;
  }
  .brand {
    position: absolute;
    left: 0; width: 1200px;
    text-align: center;
    color: var(--white);
  }
  .brand__est {
    position: absolute;
    top: 113px;
    font-family: "Montserrat", sans-serif;
    font-weight: 700;
    font-size: 14px;
    letter-spacing: 0.08em;
    color: var(--white);
  }
  .brand__est--left { left: 528px; }
  .brand__est--right { left: 672px; }
  .brand__name {
    top: 136px;
    font-family: "Oswald", sans-serif;
    font-weight: 600;
    font-size: 50px;
    letter-spacing: 0.05em;
    line-height: 1;
    text-transform: uppercase;
  }
  .brand__slogan {
    top: 214px;
    font-family: "Montserrat", sans-serif;
    font-weight: 700;
    font-size: 13px;
    letter-spacing: 0.08em;
    text-transform: uppercase;
  }
  .flourish {
    position: absolute;
    top: 150px;
    width: 156px;
    height: 62px;
    border-radius: 31px;
    background: rgba(255, 255, 255, 0.16);
  }
  .flourish--left { left: 269px; }
  .flourish--right { left: 775px; }
  .product__kind {
    position: absolute;
    left: 0; top: 262px;
    width: 1200px;
    margin: 0;
    text-align: center;
    font-family: "Lobster", cursive;
    font-weight: 400;
    font-size: 116px;
    line-height: 1;
    color: var(--ink);
  }
  .headline {
    font-family: "Graduate", serif;
    font-size: 178px;
  }
  .count {
    position: absolute;
    left: 447px; top: 770px;
    width: 255px; height: 54px;
    display: flex;
    align-items: center;
    justify-content: center;
    font-family: "Oswald", sans-serif;
    font-weight: 500;
    font-size: 27px;
    letter-spacing: 0.03em;
    color: var(--white);
  }
  .supplement {
    position: absolute;
    left: 0; top: 846px;
    width: 1200px;
    text-align: center;
    font-family: "Montserrat", sans-serif;
    font-weight: 500;
    font-size: 23px;
    letter-spacing: 0.42em;
    color: var(--white);
    text-transform: uppercase;
  }
  .claims {
    position: absolute;
    left: 0; top: 902px;
    width: 1200px;
    text-align: center;
    font-family: "Montserrat", sans-serif;
    font-weight: 700;
    font-size: 15px;
    letter-spacing: 0.2em;
    color: var(--red);
    text-transform: uppercase;
  }
</style>
</head>
<body>
<main class="label">
  <div class="label__top"></div>
  <div class="label__texture" role="img" aria-label="Speckled vintage grunge texture"></div>

  <span class="brand__est brand__est--left">EST.</span>
  <span class="brand__est brand__est--right">2020</span>
  <div class="flourish flourish--left" role="img" aria-label="Vintage scroll flourish"></div>
  <div class="flourish flourish--right" role="img" aria-label="Vintage scroll flourish"></div>
  <div class="brand brand__name">Lantern Co.</div>
  <div class="brand brand__slogan">Legends Take Root</div>

  <h1 class="product__kind">Apple Cider</h1>

  <svg class="label__art" width="1200" height="957" viewBox="0 0 1200 957" aria-label="Vinegar Gummy">
    <circle cx="142" cy="564" r="48" fill="var(--red)"/>
    <circle cx="1058" cy="564" r="48" fill="var(--red)"/>
    <polygon fill="var(--ink)" points="142,556 147,570 162,570 150,579 154,593 142,585 130,593 134,579 122,570 137,570"/>
    <polygon fill="var(--ink)" points="1058,556 1063,570 1078,570 1066,579 1070,593 1058,585 1046,593 1050,579 1038,570 1053,570"/>

    <path d="M356 562 L222 762 Q204 794 244 794 L436 794" fill="none" stroke="var(--white)" stroke-width="9" stroke-linecap="round" stroke-linejoin="round"/>
    <path d="M844 562 L978 762 Q996 794 956 794 L712 794" fill="none" stroke="var(--white)" stroke-width="9" stroke-linecap="round" stroke-linejoin="round"/>

    <path d="M447 770 L702 770 L689 797 L702 824 L447 824 L460 797 Z" fill="none" stroke="var(--white)" stroke-width="4" stroke-linejoin="round"/>
    <path d="M461 778 L688 778 L678 797 L688 816 L461 816 L471 797 Z" fill="none" stroke="var(--white)" stroke-width="2" stroke-linejoin="round"/>

    <g class="headline" text-anchor="middle">
      <text x="608" y="554" textLength="538" lengthAdjust="spacingAndGlyphs" fill="var(--red-deep)">VINEGAR</text>
      <text x="598" y="546" textLength="538" lengthAdjust="spacingAndGlyphs" fill="var(--white)" stroke="var(--white)" stroke-width="10" stroke-linejoin="round">VINEGAR</text>
      <text x="598" y="546" textLength="538" lengthAdjust="spacingAndGlyphs" fill="none" stroke="var(--red-deep)" stroke-width="2.5" stroke-linejoin="round">VINEGAR</text>

      <text x="604" y="728" textLength="442" lengthAdjust="spacingAndGlyphs" fill="var(--ink-deep)">GUMMY</text>
      <text x="594" y="720" textLength="442" lengthAdjust="spacingAndGlyphs" fill="var(--white)" stroke="var(--white)" stroke-width="10" stroke-linejoin="round">GUMMY</text>
      <text x="594" y="720" textLength="442" lengthAdjust="spacingAndGlyphs" fill="none" stroke="var(--ink-deep)" stroke-width="2.5" stroke-linejoin="round">GUMMY</text>
    </g>
  </svg>

  <div class="count">60 GUMMIES</div>
  <div class="supplement">Dietary Supplement</div>
  <div class="claims">Vegan &bull; Gluten Free &bull; Non-GMO</div>
</main>
</body>
</html>
```